Professional Business Cards for Recruiting Company

We'd like professional 2-sided business cards that reflect a color scheme that matches our website, www.quillmerbay.com, and / or logo that is attached.

Slogan used is "We Know People", but needs to be editable because we change it up to "We Match Builders", "We Speak Geek", etc.

Must includes logo, slogan, first and last name, address, email, mobile number and website address.

Files attached for ideas.

Thanks!

Contact Information for Business Card

Logo, Company name, First name, Last name, addresss, email, phone, website address.

Font styles to use
Sans Serif

Colors
0054AA
0677BA
7BADD7
CADEEF
E8F1F8

Requirements
Nice to have
• I do like the following designs. 22962062 and 22962651. Couple ideas anyway.

```html
<!DOCTYPE html>
<html lang="en">
<head>
<meta charset="utf-8">
<title>Quillmer Bay Business Cards</title>
<link href="https://fonts.googleapis.com/css2?family=Montserrat:wght@300;400;600;700&family=Roboto:wght@300;400&display=swap" rel="stylesheet">
<style>
  :root {
    --brand-blue: #1a4f93;
    --brand-blue-deep: #174a8b;
    --accent-grey: #6f7275;
    --frame-grey: #8a8c8e;
    --paper: #ffffff;
    --backdrop: #e6e6e6;
    --text-grey: #8c8c8c;
    --on-blue: #ffffff;
  }
  * { margin: 0; padding: 0; box-sizing: border-box; }
  html, body { width: 1200px; height: 802px; overflow: hidden; background: var(--backdrop); }
  .canvas { position: relative; width: 1200px; height: 802px; }

  .card {
    position: absolute; width: 540px; height: 309px; top: 246px; overflow: hidden;
    box-shadow: 0 6px 18px rgba(0,0,0,0.18);
  }
  .card-front { left: 40px; background: var(--paper); }
  .card-back { left: 620px; background: var(--brand-blue-deep); }
  .card-shapes { position: absolute; inset: 0; }

  .holder-name {
    position: absolute; right: 62px; top: 26px; text-align: right;
    font-family: "Montserrat", sans-serif; font-weight: 700; font-size: 17px;
    color: var(--brand-blue); letter-spacing: 0.3px;
  }
  .holder-role {
    display: block; font-weight: 400; font-size: 12px; color: var(--text-grey); margin-top: 2px;
  }

  .wordmark { position: absolute; left: 32px; top: 92px; color: var(--brand-blue); }
  .wordmark-name {
    font-family: "Montserrat", sans-serif; font-weight: 300; font-size: 31px; letter-spacing: 1px;
    border-bottom: 1.5px solid var(--brand-blue); padding-bottom: 2px; line-height: 1.1;
  }
  .wordmark-tagline {
    font-family: "Montserrat", sans-serif; font-weight: 600; font-size: 6.6px; letter-spacing: 1.1px; margin-top: 4px;
  }

  .address {
    position: absolute; left: 32px; top: 168px;
    font-family: "Roboto", sans-serif; font-weight: 300; font-size: 13px; line-height: 1.3; color: var(--text-grey);
  }

  .contact-list {
    position: absolute; left: 32px; bottom: 18px; list-style: none;
    font-family: "Roboto", sans-serif; font-weight: 400; font-size: 13px; color: var(--on-blue);
  }
  .contact-list li { display: flex; align-items: center; gap: 9px; line-height: 1.55; }
  .contact-list svg { width: 11px; height: 11px; flex: none; }

  .back-lockup { position: absolute; left: 70px; top: 100px; display: flex; align-items: center; gap: 18px; color: var(--on-blue); }
  .back-mark { width: 58px; height: 58px; border: 2px solid var(--on-blue); transform: rotate(45deg) scale(0.8); flex: none; }
  .back-name {
    font-family: "Montserrat", sans-serif; font-weight: 300; font-size: 36px; letter-spacing: 1px;
    border-bottom: 1.5px solid var(--on-blue); line-height: 1.1; padding-bottom: 2px;
  }
  .back-tagline { font-family: "Montserrat", sans-serif; font-weight: 600; font-size: 7.4px; letter-spacing: 1.3px; margin-top: 4px; }
  .slogan {
    position: absolute; left: 0; right: 0; top: 214px; text-align: center;
    font-family: "Montserrat", sans-serif; font-weight: 300; font-size: 16px; color: var(--on-blue);
  }
</style>
</head>
<body>
<main class="canvas">

  <section class="card card-front" aria-label="Business card front">
    <svg class="card-shapes" viewBox="0 0 540 309" aria-hidden="true">
      <polygon points="0,226 360,226 540,118 540,309 0,309" fill="var(--brand-blue)"/>
      <polygon points="540,40 540,118 430,118" fill="var(--accent-grey)"/>
      <rect x="500" y="0" width="8" height="22" fill="var(--brand-blue)"/>
      <rect x="382" y="78" width="80" height="80" fill="var(--paper)" stroke="var(--frame-grey)" stroke-width="3"/>
    </svg>

    <div class="holder-name">DANIEL MORROW<span class="holder-role">Manager</span></div>

    <div class="wordmark">
      <div class="wordmark-name">QUILLMER BAY</div>
      <div class="wordmark-tagline">TALENT SEARCH AND PLACEMENT SERVICES</div>
    </div>

    <p class="address">Your address<br>city, state, ZIP 0000</p>

    <ul class="contact-list">
      <li>
        <svg viewBox="0 0 12 12"><path d="M3 1 L5 3.5 L4 5 Q5 7 7 8 L8.5 7 L11 9 L9.5 11 Q4 10.5 1 3 Z" fill="currentColor"/></svg>
        555-014-2290
      </li>
      <li>
        <svg viewBox="0 0 12 12"><rect x="1" y="2.5" width="10" height="7" fill="none" stroke="currentColor" stroke-width="1.2"/><path d="M1 2.5 L6 7 L11 2.5" fill="none" stroke="currentColor" stroke-width="1.2"/></svg>
        info@quillmerbay.com
      </li>
      <li>
        <svg viewBox="0 0 12 12"><circle cx="6" cy="6" r="5" fill="none" stroke="currentColor" stroke-width="1.2"/><path d="M1 6 H11 M6 1 Q3 6 6 11 M6 1 Q9 6 6 11" fill="none" stroke="currentColor" stroke-width="1"/></svg>
        www.quillmerbay.com
      </li>
    </ul>
  </section>

  <section class="card card-back" aria-label="Business card back">
    <div class="back-lockup">
      <div class="back-mark"></div>
      <div>
        <div class="back-name">QUILLMER BAY</div>
        <div class="back-tagline">TALENT SEARCH AND PLACEMENT SERVICES</div>
      </div>
    </div>
    <p class="slogan">We Match Builders</p>
  </section>

</main>
</body>
</html>
```